Startup of Management Company looking for Designers!

I am looking for an upscale website. Veltrona will focus on Real Estate, Wealth Management, and Consulting,

Target Market(s)

investors, sellers of real estate, people looking to have their real estate management.
companies looking for consulting services

Number of Pages Required

5+ page

Font styles to use
Sans Serif

Requirements
Must have
• pictures, real.

```html
<!DOCTYPE html>
<html lang="en">
<head>
<meta charset="utf-8">
<title>Veltrona — Real Estate, Wealth Management &amp; Consulting</title>
<link rel="stylesheet" href="https://fonts.googleapis.com/css2?family=Poppins:wght@300;400;500;600;700&family=Playfair+Display:wght@700;800&family=Kaushan+Script&display=swap">
<style>
:root{
  --orange:#ff6a0c;
  --ink:#111111;
  --text:#8a8a8a;
  --muted:#b0b0b0;
  --line:#e8e8e8;
  --soft:#f7f7f7;
  --white:#ffffff;
  --footer:#000000;
}
*{box-sizing:border-box;margin:0;padding:0}
html,body{width:1200px;height:4135px;overflow:hidden;background:var(--white)}
body{font-family:"Poppins",sans-serif;color:var(--ink);position:relative}
.abs{position:absolute}
section,header,footer{position:absolute;left:0;width:1200px}

/* header */
.site-header{top:0;height:75px;border-top:3px solid var(--orange);background:var(--white)}
.brand{left:60px;top:20px;font-family:"Poppins",sans-serif;font-weight:600;font-size:30px;letter-spacing:2px;color:var(--ink);text-transform:uppercase}
.nav{top:0;left:549px;display:flex;height:72px;align-items:center;font-size:12px;color:#333;text-transform:uppercase}
.nav a{color:#333;text-decoration:none;margin-right:34px;position:relative}
.nav a.active{color:var(--orange)}
.nav a.active::after{content:"";position:absolute;left:0;right:0;bottom:-26px;height:3px;background:var(--orange)}
.search-icon{left:955px;top:28px}
.phone-btn{left:1001px;top:21px;width:138px;height:34px;border-radius:6px;background:var(--orange);color:var(--white);display:flex;align-items:center;justify-content:center;gap:8px;font-size:17px}

/* hero */
.hero{top:75px;height:637px;background:linear-gradient(120deg,#4a4f55 0%,#6e7276 35%,#8c9296 60%,#3c4249 100%)}
.hero-photo{inset:0}
.hero-title{left:382px;top:239px;width:436px;height:82px;background:var(--orange);border-radius:4px;color:var(--white);font-weight:700;font-size:54px;letter-spacing:3px;display:flex;align-items:center;justify-content:center}
.hero-tagline{left:281px;top:337px;width:638px;height:60px;background:rgba(40,40,40,.75);border-radius:4px;color:var(--white);font-weight:500;font-size:29px;display:flex;align-items:center;justify-content:center}
.hero-arrow{top:302px;width:36px;height:35px;display:flex;align-items:center;justify-content:center}
.hero-arrow.prev{left:60px;background:var(--orange)}
.hero-arrow.next{left:1102px;background:rgba(255,255,255,.35)}

/* shared headings */
.eyebrow{font-family:"Kaushan Script",cursive;font-size:22px;color:var(--ink)}
.section-title{font-family:"Playfair Display",serif;font-weight:800;font-size:36px;color:var(--ink);line-height:1.2}
.section-title span{color:var(--orange)}
.centered{left:0;width:1200px;text-align:center}

/* about */
.about{top:712px;height:488px;background:var(--white)}
.about-photo{left:135px;top:76px;width:359px;height:239px;border-radius:6px;background:linear-gradient(135deg,#2f3a44,#7d8a94 55%,#c9d2d8)}
.about-frame{left:220px;top:300px;width:189px;height:114px;border:2px dashed var(--orange);border-top:none;border-radius:0 0 6px 6px}
.about-inset{left:239px;top:244px;width:151px;height:151px;border-radius:6px;background:linear-gradient(135deg,#c77a45,#9b5a30)}
.about-copy{left:577px;top:76px;width:490px}
.about-copy .section-title{margin-top:4px}
.about-copy p{font-size:11.5px;line-height:18.7px;color:var(--text);margin-top:14px}
.btn-dark{display:inline-block;background:var(--ink);color:var(--white);font-size:13px;font-weight:500;text-transform:uppercase;border-radius:22px;padding:0 20px;height:45px;line-height:45px;margin-top:22px}

/* services */
.services{top:1200px;height:704px;background:var(--soft)}
.services-band{left:0;top:0;width:1200px;height:449px;background:linear-gradient(100deg,#3a3f45,#5b5f63 45%,#4a4e53 70%,#6b6f73)}
.services .eyebrow,.services .section-title{color:var(--white)}
.services-intro{top:170px;font-size:14px;line-height:24px;color:var(--white)}
.service-card{top:247px;width:292px;height:359px;background:var(--white);border-radius:8px;box-shadow:0 4px 14px rgba(0,0,0,.08);padding:8px;text-align:center}
.service-card .thumb{height:194px;border-radius:3px}
.service-card h3{font-size:17px;font-weight:600;margin-top:26px}
.service-card p{font-size:11.5px;line-height:19px;color:var(--muted);margin:10px 16px 0}
.arrow-btn{position:absolute;left:128px;bottom:-19px;width:37px;height:35px;border-radius:4px;background:var(--orange);display:flex;align-items:center;justify-content:center}

/* news */
.news{top:1904px;height:600px;background:var(--white)}
.news-mini{left:135px;width:300px;height:90px}
.news-mini .thumb{position:absolute;left:0;top:0;width:90px;height:90px;border-radius:3px}
.news-mini .date{position:absolute;left:117px;top:10px;font-size:11.5px;color:var(--orange)}
.news-mini h4{position:absolute;left:117px;top:36px;width:150px;font-size:12px;font-weight:500;line-height:22px}
.news-card{top:188px;width:286px}
.news-card .thumb{position:relative;height:195px;border-radius:3px}
.news-card .badge{position:absolute;left:9px;top:9px;background:var(--orange);color:var(--white);font-size:11px;padding:2px 6px;border-radius:2px}
.news-card h4{font-size:13.5px;font-weight:500;line-height:26px;margin-top:14px}
.news-card p{font-size:11px;line-height:20px;color:var(--muted);margin-top:10px}
.news-card .more{display:flex;align-items:center;gap:8px;font-size:11px;color:var(--orange);text-transform:uppercase;margin-top:12px}

/* testimonial */
.testimonial{top:2504px;height:539px}
.testimonial-panel{left:0;top:0;width:600px;height:539px;background:var(--orange);text-align:center;color:var(--white)}
.testimonial-panel .eyebrow,.testimonial-panel .section-title{color:var(--white)}
.avatar{left:260px;top:181px;width:80px;height:80px;border-radius:50%;border:3px solid var(--white);background:linear-gradient(135deg,#dde7ef,#9fb6c8)}
.client{left:0;width:600px;top:283px;font-size:15px;font-weight:500}
.stars{left:0;width:600px;top:309px;font-size:13px;letter-spacing:1px}
.quote{left:58px;width:484px;top:346px;font-size:11.5px;line-height:19px}
.dots{left:271px;top:449px;display:flex;gap:4px}
.dots i{width:11px;height:11px;border-radius:50%;border:1.5px solid var(--white);display:block}
.dots i.on{background:var(--white)}
.testimonial-photo{left:600px;top:0;width:600px;height:539px;background:linear-gradient(120deg,#d8d6d2,#a8927a 45%,#8a6a4a 70%,#cfcac4)}

/* contact */
.contact{top:3043px;height:592px;background:var(--white)}
.contact-intro{top:176px;font-size:14px;line-height:24px;color:var(--text)}
.field{border:1px solid #eeeeee;border-radius:4px;background:#fcfcfc;font-size:11px;color:#666;padding:0 17px;display:flex;align-items:center}
.field.area{align-items:flex-start;padding-top:14px}
.btn-submit{left:536px;top:475px;width:126px;height:43px;border-radius:22px;background:var(--ink);color:var(--white);font-size:12.5px;font-weight:500;display:flex;align-items:center;justify-content:center;text-transform:uppercase}

/* footer */
.site-footer{top:3635px;height:500px;background:var(--footer);color:var(--white)}
.footer-brand{left:60px;top:68px;font-size:31px;font-weight:600;letter-spacing:2px;color:var(--orange);text-transform:uppercase}
.contact-row{left:60px;display:flex;align-items:flex-start;gap:22px;font-size:12px;line-height:20px}
.contact-row .ico{width:29px;height:29px;border-radius:6px;background:var(--orange);display:flex;align-items:center;justify-content:center;flex:none}
.footer-col{top:86px}
.footer-col h5{font-family:"Playfair Display",serif;font-weight:700;font-size:19px;color:var(--orange)}
.footer-col ul{list-style:none;margin-top:16px}
.footer-col li{font-size:12px;line-height:26.5px}
.footer-col li::before{content:"•";margin-right:10px}
.footer-col p{font-size:11.5px;line-height:21px;margin-top:16px;width:260px}
.newsletter-input{left:887px;top:176px;width:252px;height:42px;background:var(--white);border-radius:3px;font-size:11px;color:#555;padding-left:16px;display:flex;align-items:center}
.newsletter-btn{left:887px;top:231px;width:125px;height:43px;background:var(--orange);border-radius:6px;font-size:12px;display:flex;align-items:center;justify-content:center;text-transform:uppercase}
.footer-bottom{left:0;top:353px;width:1200px;border-top:1px solid #1d1d1d}
.copyright{left:0;width:1200px;top:388px;text-align:center;font-size:10.5px;color:#777}
.socials{left:526px;top:423px;display:flex;gap:5px}
.socials span{width:32px;height:32px;border-radius:50%;display:block}
</style>
</head>
<body>

<header class="site-header">
  <div class="abs brand">Veltrona</div>
  <nav class="abs nav">
    <a class="active">Home</a><a>About</a><a>Services</a><a>News</a><a>Contact Us</a>
  </nav>
  <svg class="abs search-icon" width="16" height="16" viewBox="0 0 16 16" fill="none" stroke="#333" stroke-width="1.6"><circle cx="6.5" cy="6.5" r="5"/><path d="M10.3 10.3L15 15"/></svg>
  <div class="abs phone-btn">
    <svg width="18" height="18" viewBox="0 0 24 24" fill="#fff"><path d="M6.6 10.8a15.1 15.1 0 006.6 6.6l2.2-2.2a1 1 0 011-.25 11.4 11.4 0 003.6.57 1 1 0 011 1V20a1 1 0 01-1 1A17 17 0 013 4a1 1 0 011-1h3.5a1 1 0 011 1c0 1.25.2 2.45.57 3.6a1 1 0 01-.25 1z"/></svg>
    <span>123.456.7890</span>
  </div>
</header>

<section class="hero">
  <div class="abs hero-photo" role="img" aria-label="Business team meeting around an office table, man with glasses in foreground"></div>
  <div class="abs hero-title">VELTRONA</div>
  <div class="abs hero-tagline">The fastest way ro achive your success</div>
  <div class="abs hero-arrow prev"><svg width="10" height="14" viewBox="0 0 10 14" fill="none" stroke="#fff" stroke-width="1.5"><path d="M8 1L2 7l6 6"/></svg></div>
  <div class="abs hero-arrow next"><svg width="10" height="14" viewBox="0 0 10 14" fill="none" stroke="#fff" stroke-width="1.5"><path d="M2 1l6 6-6 6"/></svg></div>
</section>

<section class="about">
  <div class="abs about-photo" role="img" aria-label="Smiling businessman shaking hands with a colleague"></div>
  <div class="abs about-frame"></div>
  <div class="abs about-inset" role="img" aria-label="Orange-toned photo of a business handshake"></div>
  <div class="abs about-copy">
    <div class="eyebrow">About Company</div>
    <h2 class="section-title">Welcome <span>To Veltrona</span></h2>
    <p>Lorem ipsum dolor sit amet, consectetur adipiscing elit, sed do eiusmod tempor ther incididunt ut labore et dolore magna aliqua. Ut enim ad minim veniam, quis nostrud exercitation ullamco laboris nisi ut aliquip ex ea commodo consequat. Duis aute toh irure dolor in reprehenderit in voluptate velit esse cillum dolore eu fugiat nulla therf pariatur. Excepteur sint occaecat cupidatat non proident, sunt in culpa qui officia deserunt mollit anim id est laborum.</p>
    <p>Lorem ipsum dolor sit amet, consectetur adipiscing elit, sed do eiusmod tempor ther incididunt ut labore et dolore magna aliqua. Ut enim ad minim veniam, quis nostrud exercitation ullamco laboris nisi ut aliquip ex ea commodo consequat.</p>
    <span class="btn-dark">Learn More</span>
  </div>
</section>

<section class="services">
  <div class="abs services-band" role="img" aria-label="Darkened photo of colleagues working in a bright office"></div>
  <div class="abs centered eyebrow" style="top:74px">What We Do</div>
  <h2 class="abs centered section-title" style="top:106px">Our <span>Services</span></h2>
  <p class="abs centered services-intro">Lorem ipsum dolor sit amet, consectetur adipiscing elit, sed do eiusmod<br>tempor incididunt ut labore et dolore magna aliqua.</p>

  <article class="abs service-card" style="left:135px">
    <div class="thumb" role="img" aria-label="Suburban family houses with green lawn" style="background:linear-gradient(180deg,#6fa8dc,#c5d8e6 45%,#5e8f3a 75%)"></div>
    <h3>Real Estate</h3>
    <p>Lorem ipsum dolor sit amet, consectetur adipiscing elit, sed do eiusmod tempor incididunt ut labore et dolore magna.</p>
    <span class="arrow-btn"><svg width="14" height="12" viewBox="0 0 14 12" fill="none" stroke="#fff" stroke-width="1.6"><path d="M1 6h11M7.5 1.5L12 6l-4.5 4.5"/></svg></span>
  </article>
  <article class="abs service-card" style="left:454px">
    <div class="thumb" role="img" aria-label="Hand using a calculator over financial charts" style="background:linear-gradient(135deg,#d9c7b8,#b79780 50%,#6fa6c4)"></div>
    <h3>Wealth Management</h3>
    <p>Lorem ipsum dolor sit amet, consectetur adipiscing elit, sed do eiusmod tempor incididunt ut labore et dolore magna.</p>
    <span class="arrow-btn"><svg width="14" height="12" viewBox="0 0 14 12" fill="none" stroke="#fff" stroke-width="1.6"><path d="M1 6h11M7.5 1.5L12 6l-4.5 4.5"/></svg></span>
  </article>
  <article class="abs service-card" style="left:773px">
    <div class="thumb" role="img" aria-label="Two consultants talking in a lounge with grey chairs" style="background:linear-gradient(135deg,#c9cfd4,#7d8790 55%,#4f5961)"></div>
    <h3>Consulting</h3>
    <p>Lorem ipsum dolor sit amet, consectetur adipiscing elit, sed do eiusmod tempor incididunt ut labore et dolore magna.</p>
    <span class="arrow-btn"><svg width="14" height="12" viewBox="0 0 14 12" fill="none" stroke="#fff" stroke-width="1.6"><path d="M1 6h11M7.5 1.5L12 6l-4.5 4.5"/></svg></span>
  </article>
</section>

<section class="news">
  <div class="abs centered eyebrow" style="top:74px">Recent Updated</div>
  <h2 class="abs centered section-title" style="top:106px">Latest <span>News</span></h2>

  <div class="abs news-mini" style="top:188px">
    <div class="thumb" role="img" aria-label="Smartphone on a desk" style="background:linear-gradient(135deg,#8a6e5a,#3a2f2a)"></div>
    <span class="date">25 Feb 2021</span><h4>Lorem ipsum dolor sit amet, consectetur.</h4>
  </div>
  <div class="abs news-mini" style="top:311px">
    <div class="thumb" role="img" aria-label="Coffee cup and notebook on a table" style="background:linear-gradient(135deg,#e2d6c8,#9b6b4a)"></div>
    <span class="date">25 Feb 2021</span><h4>Lorem ipsum dolor sit amet, consectetur.</h4>
  </div>
  <div class="abs news-mini" style="top:435px">
    <div class="thumb" role="img" aria-label="Laptop on a wooden desk" style="background:linear-gradient(135deg,#c79d6c,#5a4330)"></div>
    <span class="date">25 Feb 2021</span><h4>Lorem ipsum dolor sit amet, consectetur.</h4>
  </div>

  <article class="abs news-card" style="left:457px">
    <div class="thumb" role="img" aria-label="Team reviewing work on a laptop in an office" style="background:linear-gradient(135deg,#e6e6e2,#9aa0a2 55%,#5b6366)"><span class="badge">25 Feb 2021</span></div>
    <h4>Lorem ipsum dolor sit amet, consect elit, sed do eiusmod tempor.</h4>
    <p>Lorem ipsum dolor sit amet, consectetur adipis cing elit, sed do eiusmod tempor incididunt.</p>
    <span class="more">Learn More <svg width="7" height="9" viewBox="0 0 7 9"><path d="M0 0l7 4.5L0 9z" fill="#ff6a0c"/></svg></span>
  </article>
  <article class="abs news-card" style="left:780px">
    <div class="thumb" role="img" aria-label="Presenter at a whiteboard with applauding audience" style="background:linear-gradient(135deg,#f1f1ee,#bfc4c2 55%,#6c7270)"><span class="badge">25 Feb 2021</span></div>
    <h4>Lorem ipsum dolor sit amet, consect elit, sed do eiusmod tempor.</h4>
    <p>Lorem ipsum dolor sit amet, consectetur adipis cing elit, sed do eiusmod tempor incididunt.</p>
    <span class="more">Learn More <svg width="7" height="9" viewBox="0 0 7 9"><path d="M0 0l7 4.5L0 9z" fill="#ff6a0c"/></svg></span>
  </article>
</section>

<section class="testimonial">
  <div class="abs testimonial-panel">
    <div class="abs centered eyebrow" style="width:600px;top:74px">Client's Feedback</div>
    <h2 class="abs centered section-title" style="width:600px;top:106px">Testimonial</h2>
    <div class="abs avatar" role="img" aria-label="Client portrait"></div>
    <div class="abs client">–&nbsp; Client's Name</div>
    <div class="abs stars">★★★★★</div>
    <p class="abs quote">Lorem ipsum dolor sit amet, consectetur adipiscing elit, sed do eiusmod tempor ther incididunt ut labore et dolore magna aliqua. Ut enim ad minim veniam, quis nostrud exercitation ullamco laboris nisi ut aliquip ex ea commodo consequat. Duis aute toh irure dolor in reprehenderit in voluptate velit esse cillum dolore.</p>
    <div class="abs dots"><i></i><i></i><i class="on"></i><i></i></div>
  </div>
  <div class="abs testimonial-photo" role="img" aria-label="Confident businessman with crossed arms in an office, colleague at laptop behind"></div>
</section>

<section class="contact">
  <div class="abs centered eyebrow" style="top:74px">Contact Us</div>
  <h2 class="abs centered section-title" style="top:116px">If you have <span>any question?</span></h2>
  <p class="abs centered contact-intro">Lorem ipsum dolor sit amet, consectetur adipiscing elit, sed do eiusmod<br>tempor incididunt ut labore et dolore magna aliqua.</p>
  <div class="abs field" style="left:231px;top:248px;width:361px;height:46px">Name &nbsp;:</div>
  <div class="abs field" style="left:608px;top:248px;width:359px;height:46px">Phone &nbsp;:</div>
  <div class="abs field" style="left:231px;top:308px;width:736px;height:45px">Email &nbsp;:</div>
  <div class="abs field area" style="left:231px;top:369px;width:736px;height:86px">Message/ Comments &nbsp;:</div>
  <div class="abs btn-submit">Submit Now</div>
</section>

<footer class="site-footer">
  <div class="abs footer-brand">Veltrona</div>
  <div class="abs contact-row" style="top:128px">
    <span class="ico"><svg width="12" height="16" viewBox="0 0 12 16" fill="#fff"><path d="M6 0a6 6 0 00-6 6c0 4.5 6 10 6 10s6-5.5 6-10a6 6 0 00-6-6zm0 8.2A2.2 2.2 0 116 3.8a2.2 2.2 0 010 4.4z"/></svg></span>
    <span>123,Address, Street Name, State<br>Name, City Name, Zipcode.</span>
  </div>
  <div class="abs contact-row" style="top:175px;align-items:center">
    <span class="ico"><svg width="14" height="14" viewBox="0 0 24 24" fill="#fff"><path d="M6.6 10.8a15.1 15.1 0 006.6 6.6l2.2-2.2a1 1 0 011-.25 11.4 11.4 0 003.6.57 1 1 0 011 1V20a1 1 0 01-1 1A17 17 0 013 4a1 1 0 011-1h3.5a1 1 0 011 1c0 1.25.2 2.45.57 3.6a1 1 0 01-.25 1z"/></svg></span>
    <span>123.456.7890</span>
  </div>
  <div class="abs contact-row" style="top:218px;align-items:center">
    <span class="ico"><svg width="14" height="11" viewBox="0 0 14 11" fill="none" stroke="#fff" stroke-width="1.4"><rect x="0.7" y="0.7" width="12.6" height="9.6"/><path d="M0.7 0.7L7 6l6.3-5.3"/></svg></span>
    <span>info@veltrona.com</span>
  </div>

  <div class="abs footer-col" style="left:337px">
    <h5>Services</h5>
    <ul><li>Real Estate</li><li>Wealth Management</li><li>Consulting</li></ul>
  </div>
  <div class="abs footer-col" style="left:613px">
    <h5>Links</h5>
    <ul><li>Home</li><li>About Us</li><li>Services</li><li>Blog</li><li>Contact Us</li></ul>
  </div>
  <div class="abs footer-col" style="left:889px">
    <h5>Stay Updated</h5>
    <p>Lorem ipsum dolor sit amet, consectetur adipiscing elit, sed do eiusmod tempor.</p>
  </div>
  <div class="abs newsletter-input">Enter Email......</div>
  <div class="abs newsletter-btn">Subcribe Now</div>

  <div class="abs footer-bottom"></div>
  <div class="abs copyright">Copyright © VELTRONA - 2021. All Right Reserved &nbsp;|&nbsp; Privacy Policy &nbsp;|&nbsp; Terms &amp; Conditions</div>
  <div class="abs socials">
    <span style="background:#3b5bb0"></span>
    <span style="background:#1da1f2"></span>
    <span style="background:#0a76b4"></span>
    <span style="background:#e1306c"></span>
  </div>
</footer>

</body>
</html>
```